Design the Mobile Version of Existing Web Based Health Platform

Loomcrest is a social business enterprise that focus on public health by applying innovative healthcare services and consumer internet technology. Loomcrest offers a personalized platform of health promotion and disease prevention that puts the individual back in control of his life.

Loomcrest is looking for a Mobile Web UX/Visual Design professional to create a mobile version of Loomcrest website platform for iPhone, iPad/tablet and Android.

Contestants must to check www.loomcrest-demo.com.br to have a better understanding of Loomcrest Platform by creating an account (it's in portuguese, but anyone can get the general idea).

The mobile version of Loomcrest should have very similar functionality and user flows. This job is not to reengineer or re-imagine Loomcrest. It is just to reformat the existing functionality so it works well on mobile devices.

This description below is to help you to understand the core features of the platform (check the attachments to see the new web design of each one):

- Personally Controlled Health Record - PCHR enables an individual to own and manage a complete, secure, digital copy of her health and wellness information.
- Health Risk Assessments - is a process to estimate the nature and probability of adverse health effects, based on personal and family historical data, behavior and environment.
- Simulation of future health - "what if analysis" that emphasizes health education and behavior change.
- Step Quests - a program that gives you the opportunity to the participant to advance his personal well-being by doing simple Step Quests
- Health Alerts and Recommendations and Missing Data - Recommendations based on Wellbeing Bureau Guidelines and Federal Wellness Review Panel (FWRP), plus notifications to update outdated information.

The deliverable for this project is a psd file with a designed mobile version of Loomcrest.

A new design of the web platform is under construction. You can also check it looking at the files attached.

Target Market(s)

people 25-40 years old, 60% female, socially engaged

Industry/Entity Type

Healthcare

Requirements
Must have
• iPhone, iPad and Android version

Design must cover all current functionalities available on the web version (please, ensure you understand all features by creating an account at www.loomcrest-demo.com.br)

- Login/Sign up
- Welcome (first assessment)
- Add to Personal Controlled Health Record (PCHR)
- Update/Remove PCHR
- List PCHR
- Riskgrid (risk assessmen results)
- Simulation
- Alerts
- Missing data
- Recommendations
- StepQuest
- Badges
- Configurations

It's important to check the attachments to see how the web platform design is evolving.

```html
<!DOCTYPE html>
<html lang="en">
<head>
<meta charset="utf-8">
<title>Loomcrest – Splash Screen</title>
<link rel="stylesheet" href="https://fonts.googleapis.com/css2?family=Inter:wght@500;600&family=Nunito:wght@700;800&display=swap">
<style>
  :root {
    --stage-bg-top: #fbfbfb;
    --stage-bg-bottom: #b8bcc1;
    --status-bar: #000000;
    --status-text: #ffffff;
    --brand-orange: #f4692a;
    --brand-orange-mid: #f67f34;
    --brand-orange-light: #f7953f;
    --brand-white: #ffffff;
  }
  * { box-sizing: border-box; margin: 0; padding: 0; }
  html, body {
    width: 1200px;
    height: 1115px;
    overflow: hidden;
  }
  body {
    background: linear-gradient(to bottom, var(--stage-bg-top) 0%, var(--stage-bg-bottom) 100%);
    display: flex;
    align-items: center;
    justify-content: center;
  }
  .splash-screen {
    width: 560px;
    height: 995px;
    display: flex;
    flex-direction: column;
    box-shadow: 0 2px 6px rgba(0,0,0,0.18);
  }
  .status-bar {
    flex: 0 0 34px;
    background: var(--status-bar);
    color: var(--status-text);
    font-family: "Inter", Helvetica, Arial, sans-serif;
    font-weight: 600;
    font-size: 21px;
    line-height: 1;
    display: flex;
    align-items: center;
    justify-content: space-between;
    padding: 0 8px;
    position: relative;
  }
  .status-left, .status-right {
    display: flex;
    align-items: center;
    gap: 8px;
  }
  .status-time {
    position: absolute;
    left: 50%;
    transform: translateX(-50%);
  }
  .status-bar svg { display: block; }
  .splash-body {
    flex: 1;
    background:
      radial-gradient(ellipse 65% 42% at 50% 52%, var(--brand-orange-light) 0%, var(--brand-orange-mid) 55%, var(--brand-orange) 100%);
    display: flex;
    flex-direction: column;
    align-items: center;
    padding-top: 296px;
  }
  .brand-square {
    width: 104px;
    height: 90px;
    background: var(--brand-white);
    border-radius: 6px;
  }
  .brand-name {
    margin-top: 16px;
    font-family: "Nunito", "Arial Rounded MT Bold", sans-serif;
    font-weight: 800;
    font-size: 80px;
    line-height: 1;
    color: var(--brand-white);
    letter-spacing: -1px;
  }
</style>
</head>
<body>
  <main class="splash-screen">
    <header class="status-bar">
      <div class="status-left">
        <svg class="signal-icon" width="30" height="14" viewBox="0 0 30 14" aria-hidden="true">
          <rect x="0" y="8" width="4" height="6" fill="#fff"/>
          <rect x="6" y="6" width="4" height="8" fill="#fff"/>
          <rect x="12" y="4" width="4" height="10" fill="#fff"/>
          <rect x="18" y="2" width="4" height="12" fill="#fff"/>
          <rect x="24" y="0" width="4" height="14" fill="#fff"/>
        </svg>
        <span class="carrier">Nova</span>
      </div>
      <span class="status-time">4:20 PM</span>
      <div class="status-right">
        <svg class="alarm-icon" width="18" height="18" viewBox="0 0 18 18" aria-hidden="true">
          <circle cx="9" cy="9" r="8" fill="#fff"/>
          <path d="M9 4v5h4" stroke="#000" stroke-width="2" fill="none"/>
        </svg>
        <svg class="location-icon" width="18" height="18" viewBox="0 0 18 18" aria-hidden="true">
          <path d="M17 1 1 8l7 2 2 7z" fill="#fff"/>
        </svg>
        <svg class="rotation-lock-icon" width="22" height="20" viewBox="0 0 22 20" aria-hidden="true">
          <path d="M18 10a8 8 0 1 1-3-6.3" stroke="#fff" stroke-width="2.2" fill="none"/>
          <path d="M13 1l4 3-4 3z" fill="#fff"/>
          <rect x="6.5" y="9" width="8" height="6" rx="1" fill="#fff"/>
          <path d="M8 9V7.5a2.5 2.5 0 0 1 5 0V9" stroke="#fff" stroke-width="1.6" fill="none"/>
        </svg>
        <svg class="battery-icon" width="36" height="16" viewBox="0 0 36 16" aria-hidden="true">
          <rect x="1" y="1" width="30" height="14" rx="2" stroke="#fff" stroke-width="2" fill="none"/>
          <rect x="4" y="4" width="24" height="8" fill="#fff"/>
          <rect x="32" y="5" width="3" height="6" fill="#fff"/>
        </svg>
      </div>
    </header>
    <section class="splash-body">
      <div class="brand-square" aria-hidden="true"></div>
      <h1 class="brand-name">loomcrest</h1>
    </section>
  </main>
</body>
</html>
```